7KT Guided Signal: Welfare - A book about Safety Messaging

Please refer to sample covers in the attached files none of which I found adequate.I would prefer a book cover that some kind of construction photo with people in it.
Book size is 6"*9"
“7KT Guided Signal: Welfare” is a short book that is intended to provide some background and explanation in support of the 7KT Welfare.com work site. The book is set up on Brindlemart.com’s pagelume site.
I would like to display the 7KT Welfare logo, title, author name on the front cover with a suitable construction oriented photo in support of that. On the back cover I’d like to show if it makes sense the essence of 7KT Welfare.com which is as follows:
7KT:
Right Messages,
Right People,
Right Time,
Right results
Prioritized
Proactive
Painless
Patented
7KT builds on the analysis of any process, near miss, accident, or incident and the subsequent repackaging of the resultant messages for delivery, audit and follow up on an ongoing basis. The messages and follow up are relentless and delivered before any subsequent events can occur. Specific and detailed messages from are managed; they are not forgotten. Quality is checked on a continuous basis.
A Safety Culture consists of the pool of ideas, thoughts, images, practices, written text, and beliefs that all constitute messages and guide our actions in the workplace. 7KT is designed to support existing practices and replace some of the less effective practices.
7KT simplifies the transmission of safety messages, information and ideas. Single messages will be easily handled and not lost in the sea of competing messages.
In its most simple form, a message is an idea a person either receives, or conceives and can communicate to another person. Messages include training, posters, hardhat stickers, safety manuals.
Updates
I would like to consider the following bylines for inclusion somewhere on the front or back cover of the book.Note that the book cover is designed to be used on PrintNook and so the cover will include the front and back of the book."The New Standard For Safety Messages Building a Culture of Confidence" Added Thursday, May 28, 2015
Target Market(s)
Safety Professionals worldwide
Industry/Entity Type
Construction
Requirements
Must have
- A back cover and be set up for Print Nook,
- The Title of the Book is 7KT Guided Signal: Welfare
Nice to have
- A color construction Photo that spans back and front covers and comforms to the theme of the book.
- Tag lines that include:
- The New Standard in Safety Messaging
- Building a Culture of Confidence

```html
<!DOCTYPE html>
<html lang="en">
<head>
<meta charset="utf-8">
<title>7KT Guided Signal: Welfare — Cover Spread</title>
<link rel="stylesheet" href="https://fonts.googleapis.com/css2?family=Roboto+Condensed:ital,wght@0,400;0,700;1,400;1,700&family=Roboto:wght@700;900&display=swap">
<style>
  :root {
    --page-bg: #ffffff;
    --sky-top: #2a6a92;
    --sky-mid: #8db7cd;
    --haze: #d9e4e6;
    --ground: #6e665a;
    --ground-dark: #3f3a33;
    --title-red: #e2231a;
    --title-yellow: #f4ee1a;
    --panel-wash: rgba(255, 255, 255, 0.42);
    --body-ink: #111111;
    --frame-line: rgba(255, 255, 255, 0.9);
    --author-ink: #d8d8d8;
    --badge-red: #d8282a;
  }
  * { box-sizing: border-box; margin: 0; padding: 0; }
  html, body {
    width: 1200px; height: 804px; overflow: hidden;
    background: var(--page-bg);
  }
  .spread { position: relative; width: 1200px; height: 804px; }

  .cover-panel {
    position: absolute; top: 68px; height: 668px; overflow: hidden;
    border: 1px solid #b9c3c8;
  }
  .back-cover { left: 67px; width: 498px; }
  .spine { left: 568px; width: 62px; }
  .front-cover { left: 633px; width: 500px; }

  .site-photo {
    position: absolute; inset: 0;
    background:
      radial-gradient(ellipse 40% 22% at 50% 70%, rgba(255,246,214,0.85), rgba(255,246,214,0) 70%),
      linear-gradient(180deg, var(--sky-top) 0%, #4d8db0 25%, var(--sky-mid) 48%, var(--haze) 64%, var(--ground) 82%, var(--ground-dark) 100%);
  }

  /* Back cover */
  .back-wash {
    position: absolute; left: 66px; top: 54px; width: 357px; height: 568px;
    background: var(--panel-wash);
  }
  .back-brand {
    position: absolute; left: 0; right: 0; top: 64px; text-align: center;
    font: 700 32px/1 "Roboto Condensed", sans-serif; color: var(--title-red);
  }
  .essence {
    position: absolute; left: 66px; top: 120px; width: 357px;
    display: grid; grid-template-columns: 1fr 1fr; column-gap: 10px;
    font: 700 17px/26.5px "Roboto Condensed", sans-serif;
    list-style: none;
  }
  .essence-rights { color: var(--title-red); text-align: center; padding-left: 20px; }
  .essence-ps { color: var(--title-yellow); text-align: center; padding-right: 10px; }
  .essence-rights, .essence-ps { list-style: none; text-shadow: 0 0 2px rgba(0,0,0,0.35); }

  .back-copy {
    position: absolute; left: 92px; top: 232px; width: 312px;
    font: italic 400 10.6px/14.6px "Roboto Condensed", sans-serif;
    color: var(--body-ink); text-align: justify;
  }
  .back-copy p { text-indent: 28px; margin-bottom: 14px; }

  /* Spine */
  .spine-mark {
    position: absolute; left: 9px; top: 6px; width: 44px; height: 44px;
    border-radius: 50%; background: var(--badge-red);
    display: flex; align-items: center; justify-content: center;
    font: 700 9px/1 "Roboto Condensed", sans-serif; color: #fff; text-align: center;
  }
  .spine-title {
    position: absolute; left: 8px; top: 66px;
    writing-mode: vertical-rl;
    font: 700 25px/46px "Roboto Condensed", sans-serif; letter-spacing: 0.5px;
    color: var(--title-yellow); white-space: nowrap;
    text-shadow: 0 0 2px rgba(0,0,0,0.4);
  }
  .spine-title .spine-title-accent { color: var(--title-red); letter-spacing: 4px; }
  .spine-author {
    position: absolute; left: 0; right: 0; bottom: 6px; text-align: center;
    font: 400 12px/19px "Roboto Condensed", sans-serif; color: #f0f0f0;
    text-shadow: 0 0 2px rgba(0,0,0,0.6);
  }

  /* Front cover */
  .front-mark {
    position: absolute; left: 207px; top: 18px; width: 86px; height: 86px;
    border-radius: 50%; background: var(--badge-red);
    display: flex; align-items: center; justify-content: center;
    font: 700 15px/1 "Roboto Condensed", sans-serif; color: #fff;
  }
  .title-frame {
    position: absolute; left: 38px; top: 107px; width: 422px; height: 197px;
    border: 2px solid var(--frame-line);
    background: rgba(255,255,255,0.12);
  }
  .title-lead {
    position: absolute; left: 0; right: 0; top: 160px; text-align: center;
    font: 700 27px/1 "Roboto Condensed", sans-serif; color: var(--title-yellow);
    text-shadow: 1px 1px 2px rgba(0,0,0,0.5);
  }
  .title-main {
    position: absolute; left: 0; right: 0; top: 188px; text-align: center;
    font: 900 74px/1 "Roboto", sans-serif; letter-spacing: 12px; padding-left: 12px;
    color: var(--title-red);
    text-shadow: 2px 3px 3px rgba(0,0,0,0.45);
  }
  .tagline {
    position: absolute; left: 0; right: 0; text-align: center;
    font: 700 22px/1 "Roboto Condensed", sans-serif;
    text-shadow: 1px 1px 2px rgba(0,0,0,0.55);
  }
  .tagline-standard { top: 316px; color: var(--title-yellow); }
  .tagline-culture { top: 346px; color: var(--title-red); }
  .front-author {
    position: absolute; left: 0; right: 0; top: 608px; text-align: center;
    font: 700 24px/1 "Roboto", sans-serif; letter-spacing: 1.5px;
    color: var(--author-ink); text-shadow: 1px 2px 2px rgba(0,0,0,0.6);
  }
</style>
</head>
<body>
<main class="spread">

  <section class="cover-panel back-cover">
    <div class="site-photo" role="img" aria-label="Construction site photo continued: drilling rig and rebar cage under blue sky with workers in orange high-visibility gear"></div>
    <div class="back-wash"></div>
    <h2 class="back-brand">7KT</h2>
    <div class="essence">
      <ul class="essence-rights">
        <li>Right Messages</li>
        <li>Right People</li>
        <li>Right Time</li>
        <li>Right results</li>
      </ul>
      <ul class="essence-ps">
        <li>Prioritized</li>
        <li>Proactive</li>
        <li>Painless</li>
        <li>Patented</li>
      </ul>
    </div>
    <div class="back-copy">
      <p>7KT builds on the analysis of any process, near miss, accident, or incident and the subsequent repackaging of the resultant messages for delivery, audit and follow up on an ongoing basis. The messages and follow up are relentless and delivered before any subsequent events can occur. Specific and detailed messages from are managed; they are not forgotten. Quality is checked on a continuous basis.</p>
      <p>A Safety Culture consists of the pool of ideas, thoughts, images, practices, written text, and beliefs that all constitute messages and guide our actions in the workplace. 7KT is designed to support existing practices and replace some of the less effective practices.</p>
      <p>7KT simplifies the transmission of safety messages, information and ideas. Single messages will be easily handled and not lost in the sea of competing messages.</p>
      <p>In its most simple form, a message is an idea a person either receives, or conceives and can communicate to another person. Messages include training, posters, hardhat stickers, safety manuals.</p>
    </div>
  </section>

  <section class="cover-panel spine">
    <div class="site-photo" role="img" aria-label="Construction site photo continued across the spine"></div>
    <div class="spine-mark">7KT Welfare</div>
    <h2 class="spine-title">7KT GUIDED SIGNAL: <span class="spine-title-accent">WELFARE</span></h2>
    <p class="spine-author">Marcel<br>R<br>Tessier<br>P.Eng</p>
  </section>

  <section class="cover-panel front-cover">
    <div class="site-photo" role="img" aria-label="Construction site photo: workers in orange high-visibility gear and hard hats guiding a rebar cage beside a drilling rig under a bright blue sky"></div>
    <div class="front-mark">7KT Welfare</div>
    <div class="title-frame"></div>
    <h1>
      <span class="title-lead">7KT GUIDED SIGNAL:</span>
      <span class="title-main">WELFARE</span>
    </h1>
    <p class="tagline tagline-standard">The New Standard in Safety Messaging</p>
    <p class="tagline tagline-culture">Building a Culture of Confidence</p>
    <p class="front-author">Marcel R Tessier P.Eng</p>
  </section>

</main>
</body>
</html>
```